Accountants Stationary Package

Letter head, compliment slip, business card, report cover

Using selected logo which will be supplied when available design with compliment slip, letter head, business card and report cover. Some information to be amended and will be supplied at revision stage, design needs to resonate with chosen logo.

Update information 1 business card - my name is "Martin Kessler" post numerals are FCA , TITLE = Managing Director, (but maybe chartered accountant) is ok, my personal mobile is 0417 58 63 14 and personal email ids martin.k@kesslerledger.com,au, I like the tag line included " everybody ....succcess" Don't want professional liability logo but ok with the PQ and tallo logo I like the colours I like the blue back where it has a soft watermark finish 2. letterheads Need logos for tallo, PQ, professional standards Needs full company name and ABN NUMmber as - Kessler Ledger Pty Limited, ACN 748 206 513 Linked in ? I am also ok with initials instead of icons for phone, email, fax mobile, etc

Industry/Entity Type

Accounting

Requirements
Must have
• Kessler Ledger Pty Limited
• ABN 480591736
• Charted accountants
• Telephone 612 48350926
• Fax 612 4859 0417
• Po Box 6841, Holtby, NSW, 2871
• Mobile 0417 586 314
• Address 42 Wenlock road, Holtby, unit 3 Wenlock Central
• Mail@kesslerledger.com.au
• Website kesslerledger.com.au
• List of services;
• Tax and Accounting
• Business Development
• Superannuation and Financial Services

```html
<!DOCTYPE html>
<html lang="en">
<head>
<meta charset="utf-8">
<title>Kessler Ledger – Business Card</title>
<link href="https://fonts.googleapis.com/css2?family=Montserrat:wght@500;600&family=Arimo:ital,wght@0,400;1,400&display=swap" rel="stylesheet">
<style>
  :root {
    --blue: #27a9e1;
    --green: #8dc63f;
    --orange: #f26531;
    --ink: #4a4a4a;
    --grey: #5c5c5c;
    --paper: #ffffff;
    --backdrop: #ebe8e4;
    --badge-dark: #111111;
    --badge-muted: #c9ccd1;
  }
  * { margin: 0; padding: 0; box-sizing: border-box; }
  html, body { width: 1200px; height: 987px; overflow: hidden; }
  body {
    background: var(--backdrop);
    font-family: "Arimo", Arial, sans-serif;
    color: var(--ink);
    position: relative;
  }
  .card {
    position: absolute;
    left: 293px;
    width: 615px;
    height: 351px;
    background: var(--paper);
    box-shadow: 0 2px 6px rgba(0,0,0,.18);
    overflow: hidden;
  }
  .card--front { top: 129px; }
  .card--back { top: 505px; }

  .brand {
    position: absolute;
    display: flex;
    align-items: center;
    gap: 18px;
  }
  .brand__mark { background: var(--blue); flex: none; }
  .brand__name {
    font-family: "Montserrat", sans-serif;
    font-weight: 600;
    color: var(--blue);
    letter-spacing: 1px;
  }
  .card--front .brand { left: 332px; top: 69px; }
  .card--front .brand__mark { width: 62px; height: 62px; }
  .card--front .brand__name { font-size: 35px; }

  .person { position: absolute; left: 37px; top: 161px; }
  .person__name {
    font-family: "Montserrat", sans-serif;
    font-weight: 600;
    font-size: 22px;
    color: var(--blue);
    letter-spacing: .5px;
    line-height: 26px;
  }
  .person__title {
    font-family: "Montserrat", sans-serif;
    font-weight: 500;
    font-size: 18px;
    color: var(--orange);
    line-height: 22px;
  }

  .tri-rule {
    position: absolute;
    left: 37px;
    width: 548px;
    height: 2px;
    display: flex;
    gap: 3px;
  }
  .tri-rule span { flex: 1; }
  .tri-rule span:nth-child(1) { background: var(--blue); }
  .tri-rule span:nth-child(2) { background: var(--green); }
  .tri-rule span:nth-child(3) { background: var(--orange); }
  .card--front .tri-rule { top: 215px; }
  .card--back .tri-rule { top: 244px; }

  .contacts {
    position: absolute;
    left: 37px;
    top: 232px;
    list-style: none;
    font-size: 16px;
    line-height: 23px;
  }
  .contacts li { display: flex; align-items: center; gap: 8px; }
  .contacts svg { width: 16px; height: 16px; fill: var(--blue); flex: none; }

  .address {
    position: absolute;
    right: 30px;
    top: 232px;
    text-align: right;
    font-size: 16px;
    line-height: 23px;
    font-style: normal;
  }

  .card--back .brand {
    left: 0; right: 0; top: 60px;
    justify-content: center;
  }
  .card--back .brand__mark { width: 92px; height: 92px; }
  .card--back .brand__name { font-size: 40px; }
  .website {
    position: absolute;
    left: 0; right: 0; top: 182px;
    text-align: center;
    font-style: italic;
    font-size: 18px;
    color: var(--grey);
  }

  .services {
    position: absolute;
    left: 38px;
    top: 259px;
    list-style: none;
    font-size: 15.5px;
    line-height: 19.5px;
    color: var(--grey);
  }
  .services li { padding-left: 14px; position: relative; }
  .services li::before {
    content: "";
    position: absolute;
    left: 0; top: 7px;
    width: 6px; height: 6px;
    border-radius: 50%;
    background: var(--blue);
  }
  .services li.cont::before { display: none; }

  .badges { position: absolute; left: 330px; top: 266px; width: 262px; height: 64px; }
  .badge { position: absolute; }
  .badge--pq { left: 10px; top: 8px; width: 62px; height: 48px; background: var(--badge-muted); }
  .badge--tallo { left: 89px; top: 3px; width: 58px; height: 58px; border-radius: 50%; background: var(--blue); }
  .badge--standards { left: 163px; top: 4px; width: 36px; height: 56px; background: var(--badge-dark); }
  .liability-note {
    position: absolute;
    left: 204px; top: 5px;
    width: 56px;
    font-size: 6px;
    line-height: 7.5px;
    color: var(--badge-dark);
  }
</style>
</head>
<body>
  <section class="card card--front" aria-label="Business card front">
    <div class="brand">
      <span class="brand__mark"></span>
      <span class="brand__name">KESSLER</span>
    </div>

    <div class="person">
      <p class="person__name">KESSLER</p>
      <p class="person__title">Charted accountant</p>
    </div>

    <div class="tri-rule"><span></span><span></span><span></span></div>

    <ul class="contacts">
      <li>
        <svg viewBox="0 0 16 16" aria-hidden="true"><path d="M3.2 1.5l2.4 2.7-1.2 1.8c.9 2 2.5 3.6 4.5 4.6l1.8-1.2 2.8 2.4-1.4 2.3C7 13.7 2.4 9.1 1 3.2z"/></svg>
        612 48350926
      </li>
      <li>
        <svg viewBox="0 0 16 16" aria-hidden="true"><path d="M4.5 0h7A1.5 1.5 0 0113 1.5v13a1.5 1.5 0 01-1.5 1.5h-7A1.5 1.5 0 013 14.5v-13A1.5 1.5 0 014.5 0zm.3 2v10.5h6.4V2zM8 13.3a.9.9 0 100 1.8.9.9 0 000-1.8z"/></svg>
        0417 586 314
      </li>
      <li>
        <svg viewBox="0 0 16 16" aria-hidden="true"><path d="M4 1h6l2 2v3H4zM1 7h14v6h-2v-2H3v2H1zm3 5h8v3H4z"/></svg>
        612 4859 0417
      </li>
      <li>
        <svg viewBox="0 0 16 16" aria-hidden="true"><path d="M1 4h14v9H1zm1.2 1.2v.4L8 9.4l5.8-3.8v-.4zm0 1.8v4.8h11.6V7L8 10.8z"/></svg>
        Mail@kesslerledger.com.au
      </li>
    </ul>

    <address class="address">
      Po Box 6841<br>
      Holtby, NSW, 2871<br>
      42 Wenlock road, Holtby<br>
      unit 3 Wenlock Central
    </address>
  </section>

  <section class="card card--back" aria-label="Business card back">
    <div class="brand">
      <span class="brand__mark"></span>
      <span class="brand__name">KESSLER</span>
    </div>
    <p class="website">kesslerledger.com.au</p>

    <div class="tri-rule"><span></span><span></span><span></span></div>

    <ul class="services">
      <li>Tax &amp; Accounting</li>
      <li>Business Development</li>
      <li>Superannuation &amp;</li>
      <li class="cont">Financial Services</li>
    </ul>

    <div class="badges">
      <span class="badge badge--pq" role="img" aria-label="PQ membership badge"></span>
      <span class="badge badge--tallo" role="img" aria-label="tallo partner badge"></span>
      <span class="badge badge--standards" role="img" aria-label="Professional standards badge"></span>
      <p class="liability-note">Liability limited by a scheme approved under Professional Standards Legislation</p>
    </div>
  </section>
</body>
</html>
```